Roving Kneadery Business Cards

Hi Bogdan,
Thank you for designing my awesome logo! It's awesome. Now I need help in designing my business card. The business card is 3.5" x 2.0". I tried downloading my logo to PressLoom to make my business cards but the design would not fit to scale. Also I would like to have my email included tessa@rovingkneadery-example.com
On the backside of my business card I would like to have a appointment reminder on the back side of my business card
listing a space to record client's name, date, time, of appointment.
Also, I made a car magnet at Press Loom with my logo but I would like to change the width of Roving Kneadery and the sentence When worries stack on worries, you knead to set aside a pause to be the width of the logo space. It's hard to read it on the magnet from a distance. I would also like to include my email address tessa@rovingkneadery-example.com

If it is to hard to fit all of that information in the space maybe I could have the logo as two separate downloads. One with the logo picture, the name of the business, Roving Kneadery and the sentence When worries stack on worries, you knead to set aside a pause. The other download just listing my business name, my phone number, my email address, and services offered. Thanks- Henrietta:)

Reason: Hi Bogdan, I have extended the deadline by 7 days so that you do not feel rushed to get the business card project done by Wednesday. The changes that I need done are: 1. Please enlarge the sentence to be the width of the business card. The Roving Kneadery does not to be the width of the business card just the sentence. 2. The curve on the business card if you can change that curve to sky blue and not black. 3. Change the words phone, email, web address, to just icons of a phone, envelope, and the web symbol. 4. Also put my phone, email, web address on the back of my business card. Thanks, Henrietta

```html
<!DOCTYPE html>
<html lang="en">
<head>
<meta charset="utf-8">
<title>Roving Kneadery Business Cards</title>
<link rel="stylesheet" href="https://fonts.googleapis.com/css2?family=Questrial&family=Arimo:wght@400;700&display=swap">
<style>
  :root {
    --orange: #e58f24;
    --grey-band: #4b4b4d;
    --ink: #1c1c1c;
    --text: #444446;
    --rule: #5a5a5a;
    --card: #ffffff;
    --bg-light: #b9b9b9;
    --bg-dark: #5e5e5e;
  }
  * { box-sizing: border-box; margin: 0; padding: 0; }
  html, body { width: 1200px; height: 1000px; overflow: hidden; }
  body {
    background: linear-gradient(120deg, var(--bg-light) 0%, #8e8e8e 45%, var(--bg-dark) 100%);
    font-family: "Questrial", "Arimo", sans-serif;
    position: relative;
  }
  .card {
    position: absolute;
    top: 341px;
    width: 543px;
    height: 318px;
    background: var(--card);
    box-shadow: 0 2px 6px rgba(0,0,0,.35);
    overflow: hidden;
  }
  .card--front { left: 45px; }
  .card--back { left: 616px; }
  .card__band { position: absolute; left: 0; bottom: 0; width: 543px; height: 40px; }

  .brand { position: absolute; }
  .brand__name {
    font-family: "Arimo", sans-serif;
    font-weight: 700;
    color: var(--orange);
    white-space: nowrap;
  }
  .brand__tagline {
    font-family: "Arimo", sans-serif;
    font-weight: 700;
    color: var(--ink);
    line-height: 1.05;
    white-space: nowrap;
    border-bottom: 2px solid var(--orange);
    padding-bottom: 2px;
  }
  .card--front .brand { left: 55px; top: 208px; width: 220px; }
  .card--front .brand__name { font-size: 24px; }
  .card--front .brand__tagline { font-size: 12.5px; margin-top: 3px; }
  .brand__mark {
    position: absolute;
    left: 117px; top: 100px;
    width: 86px; height: 86px;
    border-radius: 50%;
    background: var(--orange);
  }

  .person { position: absolute; left: 290px; top: 36px; }
  .person__name { font-size: 21px; color: var(--orange); letter-spacing: .5px; }
  .person__role { font-size: 13px; color: var(--ink); margin-top: 2px; }

  .contacts { position: absolute; left: 290px; top: 194px; list-style: none; font-size: 13.5px; color: var(--text); }
  .contacts li { display: flex; align-items: flex-start; gap: 8px; line-height: 17px; }
  .contacts svg { flex: none; margin-top: 2px; }

  .appointment__title { position: absolute; left: 56px; top: 32px; font-size: 29px; color: var(--orange); letter-spacing: .5px; }
  .card--back .brand { left: 285px; top: 28px; width: 210px; }
  .card--back .brand__name { font-size: 23px; }
  .card--back .brand__tagline { font-size: 12px; margin-top: 2px; }

  .field { position: absolute; left: 53px; width: 438px; border-bottom: 1.5px solid var(--rule); font-size: 17px; color: var(--text); height: 26px; }
  .field--name { top: 118px; }
  .field--when { top: 165px; }
  .field--when span:last-child { position: absolute; left: 265px; }
  .field--blank { top: 205px; }
  .appointment__note { position: absolute; left: 0; width: 543px; top: 248px; text-align: center; font-size: 15.5px; color: var(--text); line-height: 18px; }
</style>
</head>
<body>

<section class="card card--front">
  <div class="brand__mark" role="img" aria-label="Brand illustration area"></div>
  <div class="brand">
    <div class="brand__name">Roving Kneadery</div>
    <div class="brand__tagline">When worries stack on worries<br>you knead to set aside a pause</div>
  </div>

  <div class="person">
    <div class="person__name">Marcus Hollen</div>
    <div class="person__role">Managing director</div>
  </div>

  <ul class="contacts">
    <li>
      <svg width="13" height="13" viewBox="0 0 13 13"><rect width="13" height="13" rx="2" fill="var(--orange)"/><path d="M4 3l1.5 0 .6 2-1 .8c.5 1.1 1.3 1.9 2.3 2.4l.8-1 2 .6V9.5c-3.5.3-6.6-2.8-6.2-6.5z" fill="#fff"/></svg>
      <span>555-014-2290</span>
    </li>
    <li>
      <svg width="13" height="13" viewBox="0 0 13 13"><rect width="13" height="13" rx="2" fill="var(--orange)"/><rect x="2.5" y="3.5" width="8" height="6" fill="none" stroke="#fff" stroke-width="1.1"/><path d="M2.5 3.5l4 3.2 4-3.2" fill="none" stroke="#fff" stroke-width="1.1"/></svg>
      <span>tessa@rovingkneadery-example.com</span>
    </li>
    <li>
      <svg width="13" height="13" viewBox="0 0 13 13"><rect width="13" height="13" rx="2" fill="var(--orange)"/><circle cx="6.5" cy="6.5" r="4" fill="none" stroke="#fff" stroke-width="1"/><path d="M2.5 6.5h8M6.5 2.5c-2 2.4-2 5.6 0 8M6.5 2.5c2 2.4 2 5.6 0 8" fill="none" stroke="#fff" stroke-width=".9"/></svg>
      <span>rovingkneadery-example.com</span>
    </li>
    <li>
      <svg width="13" height="13" viewBox="0 0 13 13"><rect width="13" height="13" rx="2" fill="var(--orange)"/><path d="M6.5 2.2a3 3 0 0 1 3 3c0 2.2-3 5.6-3 5.6s-3-3.4-3-5.6a3 3 0 0 1 3-3z" fill="#fff"/><circle cx="6.5" cy="5.2" r="1.1" fill="var(--orange)"/></svg>
      <span>17 Alder Lane,<br>City name, PO Box 4410</span>
    </li>
  </ul>

  <svg class="card__band" viewBox="0 0 543 40" preserveAspectRatio="none">
    <rect x="0" y="20" width="543" height="20" fill="var(--grey-band)"/>
    <path d="M0 40V20h330c40 0 70 2 95 20z" fill="#fff"/>
    <path d="M0 40V20h300c40 0 65 4 88 20z" fill="var(--orange)"/>
    <path d="M300 20c40 0 66 5 88 20h8c-24-15-50-20-88-20z" fill="#fff"/>
  </svg>
</section>

<section class="card card--back">
  <div class="appointment__title">Appointment</div>
  <div class="brand">
    <div class="brand__name">Roving Kneadery</div>
    <div class="brand__tagline">When worries stack on worries<br>you knead to set aside a pause</div>
  </div>

  <div class="field field--name"><span>Name:</span></div>
  <div class="field field--when"><span>Date:</span><span>Time:</span></div>
  <div class="field field--blank"></div>
  <p class="appointment__note">If unable to keep this appointment, please contact us<br>as soon as possible</p>

  <svg class="card__band" viewBox="0 0 543 40" preserveAspectRatio="none">
    <rect x="0" y="20" width="543" height="20" fill="var(--grey-band)"/>
    <path d="M0 40V20h330c40 0 70 2 95 20z" fill="#fff"/>
    <path d="M0 40V20h300c40 0 65 4 88 20z" fill="var(--orange)"/>
  </svg>
</section>

</body>
</html>
```